Business card design Tondavex

We need a business card for TONDAvex aimport and distribution company which sells personnel weight lifting accessories, mainly the varnop brand of product using our current logo. This design should represent class and a ruggard feel.

Target Market(s)

Weight lifters, crossfitters and other lifting sports

Industry/Entity Type

Weight

Contact Information for Business Card

TONDAvex, Dean Holloway, Cell: 027 815 962, Email: tondavex@mailbox.example, www.tondavex.example.nz

Requirements
Nice to have
• a good looking business card

```html
<!DOCTYPE html>
<html lang="en">
<head>
<meta charset="utf-8">
<title>Tondavex Business Card</title>
<link rel="stylesheet" href="https://fonts.googleapis.com/css2?family=Arimo:wght@400;700&family=Italianno&display=swap">
<style>
  :root {
    --page-bg: #e6e6e6;
    --card-bg: #f1f1f1;
    --ink: #1d1d1d;
    --brand-blue: #1d4f8c;
    --band-yellow: #fbb726;
    --band-orange: #f58a34;
    --band-red: #e9383d;
    --band-pink: #e73b8f;
    --band-purple: #8c3f97;
    --band-blue: #2a5aa8;
    --band-sky: #12a8e0;
    --band-green: #8cc152;
    --burst-red: #e8383a;
  }
  * { box-sizing: border-box; margin: 0; padding: 0; }
  html, body { width: 1200px; height: 900px; overflow: hidden; }
  body {
    background: var(--page-bg);
    font-family: "Arimo", Arial, sans-serif;
    color: var(--ink);
    position: relative;
  }
  .card {
    position: absolute;
    top: 150px;
    width: 360px;
    height: 600px;
    background: var(--card-bg);
    box-shadow: 0 6px 18px rgba(0,0,0,0.18);
    overflow: hidden;
  }
  .card--front { left: 180px; }
  .card--back { left: 660px; }

  .colour-rail {
    position: absolute;
    left: 0; top: 0;
    width: 26px; height: 100%;
    display: flex;
    flex-direction: column;
  }
  .colour-rail span { display: block; flex: 1; }
  .colour-rail .rail-yellow { background: var(--band-yellow); }
  .colour-rail .rail-orange { background: var(--band-orange); }
  .colour-rail .rail-red { background: var(--band-red); }
  .colour-rail .rail-pink { background: var(--band-pink); }
  .colour-rail .rail-purple { background: var(--band-purple); }
  .colour-rail .rail-blue { background: var(--band-blue); }
  .colour-rail .rail-sky { background: var(--band-sky); }
  .colour-rail .rail-green { background: var(--band-green); flex: 2.2; }

  .brand-name {
    font-family: "Arimo", Arial, sans-serif;
    font-weight: 700;
    color: var(--brand-blue);
    letter-spacing: 0.5px;
    display: flex;
    align-items: center;
    gap: 10px;
  }
  .brand-name .brand-square {
    width: 18px; height: 18px;
    background: var(--brand-blue);
  }
  .card--front .brand-name {
    position: absolute;
    top: 62px; right: 34px;
    font-size: 34px;
  }

  .holder-name {
    position: absolute;
    top: 150px; left: 62px;
    font-family: "Italianno", cursive;
    font-size: 46px;
    letter-spacing: 4px;
  }

  .contact-list {
    position: absolute;
    top: 250px; left: 62px;
    list-style: none;
    font-size: 17px;
    line-height: 1.5;
  }
  .contact-list li { display: flex; align-items: center; gap: 10px; }
  .contact-tag {
    width: 14px; height: 14px;
    border-radius: 3px;
    color: #fff;
    font-size: 10px;
    font-weight: 700;
    display: flex; align-items: center; justify-content: center;
  }
  .contact-tag--phone { background: var(--band-red); }
  .contact-tag--email { background: var(--band-green); }
  .contact-tag--web { background: var(--band-sky); }

  .sale-burst {
    position: absolute;
    left: 70px; bottom: 60px;
    width: 130px; height: 130px;
  }

  .card--back .back-mark {
    position: absolute;
    left: 50%; top: 50%;
    transform: translate(-50%, -50%);
    display: flex;
    flex-direction: column;
    align-items: center;
    gap: 12px;
  }
  .card--back .brand-name { font-size: 40px; }
  .spectrum-line { display: flex; width: 250px; height: 6px; }
  .spectrum-line span { flex: 1; }
  .spectrum-line .line-green { background: var(--band-green); flex: 2; }
  .spectrum-line .line-sky { background: var(--band-sky); }
  .spectrum-line .line-blue { background: var(--band-blue); }
  .spectrum-line .line-purple { background: var(--band-purple); }
  .spectrum-line .line-pink { background: var(--band-pink); }
  .spectrum-line .line-red { background: var(--band-red); }
  .spectrum-line .line-orange { background: var(--band-orange); }
  .spectrum-line .line-yellow { background: var(--band-yellow); }
</style>
</head>
<body>
  <section class="card card--front" aria-label="Business card front">
    <div class="colour-rail" aria-hidden="true">
      <span class="rail-yellow"></span>
      <span class="rail-orange"></span>
      <span class="rail-red"></span>
      <span class="rail-pink"></span>
      <span class="rail-purple"></span>
      <span class="rail-blue"></span>
      <span class="rail-sky"></span>
      <span class="rail-green"></span>
    </div>

    <div class="brand-name"><span class="brand-square"></span>TONDAvex</div>

    <p class="holder-name">Dean Holloway</p>

    <ul class="contact-list">
      <li><span class="contact-tag contact-tag--phone">t</span>027 815 962</li>
      <li><span class="contact-tag contact-tag--email">e</span>tondavex@mailbox.example</li>
      <li><span class="contact-tag contact-tag--web">w</span>www.tondavex.example.nz</li>
    </ul>

    <svg class="sale-burst" viewBox="0 0 130 130" aria-hidden="true">
      <g fill="var(--burst-red)">
        <rect x="19" y="19" width="92" height="92" transform="rotate(0 65 65)"/>
        <rect x="19" y="19" width="92" height="92" transform="rotate(15 65 65)"/>
        <rect x="19" y="19" width="92" height="92" transform="rotate(30 65 65)"/>
        <rect x="19" y="19" width="92" height="92" transform="rotate(45 65 65)"/>
        <rect x="19" y="19" width="92" height="92" transform="rotate(60 65 65)"/>
        <rect x="19" y="19" width="92" height="92" transform="rotate(75 65 65)"/>
      </g>
    </svg>
  </section>

  <section class="card card--back" aria-label="Business card back">
    <div class="back-mark">
      <div class="brand-name"><span class="brand-square"></span>TONDAvex</div>
      <div class="spectrum-line" aria-hidden="true">
        <span class="line-green"></span>
        <span class="line-sky"></span>
        <span class="line-blue"></span>
        <span class="line-purple"></span>
        <span class="line-pink"></span>
        <span class="line-red"></span>
        <span class="line-orange"></span>
        <span class="line-yellow"></span>
      </div>
    </div>
  </section>
</body>
</html>
```